Lindenhof Köln, Greta Wommer sucht Design
Zielgruppe
Ich mache:
1. (lebendige) Stadtführungen bzw. Gästeführung in jeder Hinsicht -> in Köln für kleine und große Gruppen und vielfältige, individuelle Themen (bei größeren Gruppen setze ich zusätzliche Guides ein, so dass ich Veranstaltungen bis 300 Personen managen kann)
2. VIP-Gästebetreuung
3. 'Rundum-Sorglos-Pakete' = komplette Eventplanung und -durchführung, d. h. Programmerstellung nach Anzahl Teilnehmer, Budget und Zeitrahmen, einschließlich Auswahl Restaurants etc. und ggfls. Bereitstellung von Limousinen, Bussen oder anderen Fahrzeugen
4. Stadtrundfahrten (dazu biete ich Fahrzeuge unterschiedlicher Größe an, oder steige als Tour-Guide in den vorhandenen Bus einer Gruppe für die Stadtrundfahrt zu)
5. Schiffstouren
6. Komplett-Planung und Durchführung von Rahmen- oder Partnerprogrammen für Firmen, deren Kunden, Mitarbeiter oder Gäste am Rande einer Tagung, Konferenz etc. unterhalten werden sollen (z. B. eine Stadtführung nach der Konferenz und vor dem Abendessen)
7. Auch Halbtages- oder Ganztagesprogramme
Zielgruppe:
Ich arbeite zwar sehr viel für private Gruppe, die möchte ich unbedingt weiterhin ansprechen, aber zunehmend auch Firmen, da ich im Bereich der VIP-Gästebetreuung und 'Rundum-Sorglos-Planung' auf zahlreiche, sehr namhafte Referenzen verweisen kann.
a) Private Gruppen (für herkömmliche Stadtführung, -rundfahrt, Schiffstour im Rahmen von diversen Anlässen)
b) Firmen (für Kundenveranstaltungen, Firmenfeiern, Rahmenprogramm während Konferenz etc., Partnerprogramm (d. h. während die Konferenzteilnehmer tagen, kümmere ich mich um die mitgereisten Partner)
c) große namhafte Hotels, die ihren Gästen eine Gästeführerin vermitteln möchten
Aufgabenstellung
Ich wünsche mir, dass aus dem Logo hervorgeht, dass ich (zertifizierte) Stadtführerin (=Gästeführerin) in Köln bin und lege Wert darauf, dass mein Design vor allem Kompetenz, Professionalität, Innovation und Vertrauen ausstrahlt.
Bei Stadtführern in Köln findet sich im Logo meist der Kölner Dom (wie bei mir aktuell auch) oder das Stadtwappen Kölns, das schwarz-weiß-rot ist. Das Stadtwappen möchte ich auf KEINEN Fall, der Dom ist immer gut aber nicht zwingend.
Auf meiner Website www.lindenhof-koeln.de habe ich mit den Farben schwarz, weinrot und grau gearbeitet. Das gefällt mir noch immer, ist aber nicht in Stein gemeißelt. Ich bevorzuge auf jeden Fall KLARE Farben und ein KLARES Design. Eher minimalistisch als verschnörkelt.

```html
<!DOCTYPE html>
<html lang="de">
<head>
<meta charset="utf-8">
<title>Lindenhof Köln – Greta Wommer</title>
<link rel="stylesheet" href="https://fonts.googleapis.com/css2?family=Roboto+Slab:wght@300;400;500&display=swap">
<style>
  :root {
    --paper: #ffffff;
    --ink: #111111;
    --wine: #9e1916;
  }
  html, body {
    margin: 0;
    padding: 0;
    overflow: hidden;
    background: var(--paper);
  }
  .card {
    position: relative;
    width: 1200px;
    height: 809px;
    background: var(--paper);
    font-family: "Roboto Slab", Georgia, serif;
    color: var(--ink);
    overflow: hidden;
  }
  .brand {
    position: absolute;
    top: 200px;
    left: 0;
    width: 1200px;
    display: flex;
    align-items: center;
    justify-content: center;
    gap: 28px;
  }
  .brand-dot {
    width: 106px;
    height: 106px;
    border-radius: 50%;
    background: var(--wine);
    flex: none;
  }
  .brand-name {
    font-weight: 500;
    font-size: 64px;
    line-height: 1;
    color: var(--ink);
    letter-spacing: 0.5px;
  }
  .person {
    position: absolute;
    top: 386px;
    left: 0;
    width: 1200px;
    text-align: center;
  }
  .person-name {
    margin: 0;
    font-weight: 400;
    font-size: 54px;
    line-height: 1.2;
  }
  .person-title {
    margin: 14px 0 0;
    font-weight: 300;
    font-size: 25px;
    line-height: 1.2;
  }
  .contact {
    position: absolute;
    top: 652px;
    left: 105px;
    right: 103px;
    display: flex;
    justify-content: space-between;
    font-weight: 300;
    font-size: 34px;
    line-height: 1.2;
  }
  .footer-band {
    position: absolute;
    left: 0;
    bottom: 0;
    width: 1200px;
    height: 48px;
    background: var(--wine);
  }
</style>
</head>
<body>
  <div class="card">
    <div class="brand">
      <span class="brand-dot"></span>
      <span class="brand-name">Lindenhof Köln</span>
    </div>

    <div class="person">
      <h1 class="person-name">Greta Wommer</h1>
      <p class="person-title">Zertifizierte Gästeführerin DIN EN 155</p>
    </div>

    <div class="contact">
      <span class="contact-email">kontakt@lindenhof-koeln.de</span>
      <span class="contact-phone">(0) 170 / 5 218 644</span>
    </div>

    <div class="footer-band"></div>
  </div>
</body>
</html>
```